Larkfield Holdings Template for Power Point

Need these all files converted and reformatted o power points to copy look and feel of website . http://larkfieldholdings.example

Target Market(s)

Real Estate

Requirements
Must have
• Congruent with LarkfieldHoldings.example

```html
<!DOCTYPE html>
<html lang="en">
<head>
<meta charset="utf-8">
<title>Larkfield Holdings – Scope of Work</title>
<link rel="stylesheet" href="https://fonts.googleapis.com/css2?family=Open+Sans:wght@400;600;700&family=Roboto+Condensed:wght@400;700&display=swap">
<style>
:root{
  --black:#0d0d0d;
  --ink:#1d1d1d;
  --gold:#f5c518;
  --amber:#e9a31b;
  --white:#ffffff;
  --paper:#ffffff;
  --canvas:#ffffff;
  --muted:#6b6b6b;
  --rule:#d6d6d6;
  --head:"Roboto Condensed", Arial, sans-serif;
  --body:"Open Sans", Arial, sans-serif;
}
*{box-sizing:border-box;margin:0;padding:0}
html,body{width:1200px;height:4200px;overflow:hidden;background:var(--canvas)}
.deck{position:relative;width:1200px;height:4200px;font-family:var(--body);color:var(--ink)}
.slide{position:absolute;width:570px;height:428px;overflow:hidden;background:var(--paper);box-shadow:0 1px 4px rgba(0,0,0,.28)}
.c1{left:20px}.c2{left:610px}
.r1{top:34px}.r2{top:496px}.r3{top:958px}.r4{top:1420px}.r5{top:1882px}
.r6{top:2344px}.r7{top:2806px}.r8{top:3268px}.r9{top:3730px}
.dark{background:var(--black);color:var(--white)}

/* brand stand-in */
.brand{display:flex;align-items:center;gap:8px;font-family:var(--head);font-weight:700;white-space:nowrap}
.brand-dot{width:14px;height:14px;border-radius:50%;background:var(--gold);flex:none}
.brand-box{position:absolute;background:var(--white);color:var(--ink);display:flex;align-items:center;justify-content:center;box-shadow:0 1px 4px rgba(0,0,0,.3)}
.brand-box .brand{font-size:15px;color:var(--ink)}

/* cover */
.cover-brand{position:absolute;left:0;right:0;top:92px;justify-content:center;font-size:32px;color:var(--white)}
.cover-brand .brand-dot{width:22px;height:22px}
.cover-title{position:absolute;left:0;right:0;top:212px;text-align:center;font-family:var(--head);font-size:52px;letter-spacing:1px;color:var(--white)}
.cover-title.gold{color:var(--gold);top:196px}
.cover-foot{position:absolute;left:0;right:0;top:350px;text-align:center}
.cover-foot strong{display:block;font-size:14px;font-weight:700}
.cover-foot span{display:block;font-size:11px;margin-top:3px}
.squares{position:absolute;right:16px;top:12px;display:flex;gap:5px}
.squares i{display:block;width:12px;height:12px;background:var(--gold)}

/* photos */
.photo{position:absolute}
.ph-house{background:linear-gradient(180deg,#8fa9b8 0%,#9fb4a8 28%,#7d4a36 42%,#8a5340 58%,#5d7d3a 70%,#4f7430 100%)}
.ph-yard{background:linear-gradient(180deg,#4d6b2f 0%,#6b5a3e 45%,#8a4f3a 60%,#5f7b35 100%)}
.ph-wood{background:linear-gradient(90deg,#6b4a2e,#8d6840 40%,#5c3f26 70%,#7a5836)}
.ph-room{background:linear-gradient(180deg,#e7e4de 0%,#d9d4ca 65%,#b8ab96 100%)}
.ph-oldroom{background:linear-gradient(180deg,#d8a24a 0%,#c58b3a 55%,#7a4b2a 100%)}
.ph-kitchen{background:linear-gradient(180deg,#f0efec 0%,#dcdcdc 40%,#3a3a3a 52%,#e8e8e8 60%,#bfbfbf 100%)}
.ph-oldkitchen{background:linear-gradient(180deg,#a7764a 0%,#7d5632 50%,#5a3c22 100%)}
.ph-bath{background:linear-gradient(180deg,#f2f2f0 0%,#e2e2de 60%,#cfcfc8 100%)}
.ph-oldbath{background:linear-gradient(180deg,#e8e1c8 0%,#d8cfae 60%,#bfb18a 100%)}
.ph-bed{background:linear-gradient(180deg,#e9e9e9 0%,#d7d7d5 70%,#b9b4aa 100%)}
.ph-oldbed{background:linear-gradient(180deg,#cfc6b0 0%,#b7ab8c 60%,#7d8fa8 100%)}
.ph-equip{background:linear-gradient(180deg,#9aa0a3 0%,#7f8588 60%,#5f6467 100%)}
.ph-panel{background:linear-gradient(180deg,#c9c9c5 0%,#a9aaa6 100%)}
.ph-tank{background:linear-gradient(180deg,#8e7a5e 0%,#b9b2a3 50%,#7d6c55 100%)}

.grid4 .photo{width:270px;height:189px}
.g-tl{left:10px;top:10px}.g-tr{left:290px;top:10px}
.g-bl{left:10px;top:207px}.g-br{left:290px;top:207px}
.tag{position:absolute;background:var(--black);color:var(--white);font-family:var(--head);font-weight:700;font-size:11px;letter-spacing:.5px;padding:3px 9px}
.page-note{position:absolute;right:12px;bottom:5px;font-size:8px;color:var(--muted)}

/* contact */
.contact{background:var(--gold)}
.contact-top{left:0;top:0;width:570px;height:100px}
.contact-title{position:absolute;left:22px;top:196px;font-family:var(--head);font-weight:700;font-size:40px;color:var(--white)}
.contact-list{position:absolute;left:260px;top:168px;list-style:none}
.contact-list li{display:flex;align-items:center;gap:12px;font-size:15px;font-weight:600;color:var(--ink);margin-bottom:14px;line-height:1.25}
.ico{width:28px;height:28px;border-radius:50%;background:var(--ink);display:flex;align-items:center;justify-content:center;flex:none}
.contact-foot{position:absolute;left:0;bottom:0;width:570px;height:46px;background:var(--black);display:flex;align-items:center;gap:7px;padding-left:20px}
.contact-foot i{display:block;width:20px;height:20px;background:var(--gold)}

/* property info */
.prop-band{position:absolute;left:0;top:0;width:570px;height:80px;background:var(--black);color:var(--white);padding:14px 0 0 22px}
.prop-band h2{font-family:var(--head);font-weight:700;font-size:21px;letter-spacing:.3px}
.prop-band p{font-family:var(--head);font-weight:700;font-size:17px;margin-top:2px}
.prop-table{position:absolute;top:254px;width:250px;font-size:9.5px}
.prop-table div{display:flex;justify-content:space-between;padding:3px 0;border-bottom:1px solid #eee}
.prop-table .hd{color:var(--amber);font-weight:700;border-bottom:none}
.prop-table .total{color:var(--amber);font-weight:700}

/* caption */
.caption{position:absolute;left:128px;top:322px;width:430px;height:62px;background:rgba(10,10,10,.88);color:var(--white);font-family:var(--head);font-size:17px;line-height:1.3;padding:8px 14px}

/* work slides */
.work-head{position:absolute;left:0;top:16px;width:570px;height:62px;background:var(--black);color:var(--white);font-family:var(--head);font-size:24px;padding:16px 0 0 22px}
.work-head.tall{height:74px;padding-top:8px;line-height:1.2}
.ticks{list-style:none;font-size:10.5px;line-height:16px}
.ticks li{position:relative;padding-left:14px}
.ticks li::before{content:"✓";position:absolute;left:0;top:0;color:var(--ink);font-weight:700}
.col{position:absolute}
.subhead{font-family:var(--head);font-weight:700;font-size:13px;margin-bottom:3px}
.subhead.amber{color:var(--amber)}

/* bedrooms */
.bed-panel{position:absolute;left:0;top:96px;width:570px;height:332px;background:var(--black)}
.bed-card{position:absolute;display:flex;background:var(--white)}
.bed-card .photo{position:relative;width:110px;height:100%;flex:none}
.bed-card .txt{padding:8px 10px}
.bed-card .ticks{font-size:9.5px;line-height:14px}
</style>
</head>
<body>
<div class="deck">

  <!-- Row 1 -->
  <section class="slide dark c1 r1">
    <div class="brand cover-brand"><span class="brand-dot"></span>Larkfield Holdings</div>
    <h1 class="cover-title">SCOPE OF WORK</h1>
    <div class="cover-foot"><strong>Providing Turnkey Properties In</strong><span>Memphis | Dallas | Houston | Little Rock | Oklahoma City | St. Louis | Tulsa</span></div>
  </section>

  <section class="slide dark c2 r1">
    <div class="brand-box" style="left:18px;top:14px;width:160px;height:64px"><div class="brand"><span class="brand-dot"></span>Larkfield Holdings</div></div>
    <div class="squares"><i></i><i></i><i></i><i></i><i></i></div>
    <h1 class="cover-title gold">SCOPE OF WORK</h1>
    <div class="cover-foot"><strong>Providing Turnkey Properties In</strong><span>Memphis | Dallas | Houston | Little Rock | Oklahoma City | St. Louis | Tulsa</span></div>
  </section>

  <!-- Row 2 -->
  <section class="slide contact c1 r2">
    <div class="photo ph-wood contact-top" role="img" aria-label="Wood plank texture band"></div>
    <div class="brand-box" style="left:14px;top:14px;width:150px;height:72px"><div class="brand"><span class="brand-dot"></span>Larkfield Holdings</div></div>
    <h2 class="contact-title">Contact Us!</h2>
    <ul class="contact-list">
      <li><span class="ico"><svg width="14" height="14" viewBox="0 0 24 24"><path fill="#fff" d="M6.6 10.8a15.1 15.1 0 0 0 6.6 6.6l2.2-2.2c.3-.3.7-.4 1-.2 1.1.4 2.3.6 3.6.6.6 0 1 .4 1 1V20c0 .6-.4 1-1 1A17 17 0 0 1 3 4c0-.6.4-1 1-1h3.5c.6 0 1 .4 1 1 0 1.3.2 2.5.6 3.6.1.3 0 .7-.2 1z"/></svg></span>555-014-2290</li>
      <li><span class="ico"><svg width="14" height="14" viewBox="0 0 24 24"><circle cx="12" cy="12" r="9" fill="none" stroke="#fff" stroke-width="2"/><path d="M3 12h18M12 3c3 3 3 15 0 18M12 3c-3 3-3 15 0 18" fill="none" stroke="#fff" stroke-width="1.6"/></svg></span>www.LarkfieldHoldings.example</li>
      <li><span class="ico"><svg width="14" height="14" viewBox="0 0 24 24"><path fill="#fff" d="M12 2a7 7 0 0 0-7 7c0 5 7 13 7 13s7-8 7-13a7 7 0 0 0-7-7zm0 9.5A2.5 2.5 0 1 1 12 6.5a2.5 2.5 0 0 1 0 5z"/></svg></span>48 Ridgeway Court,<br>Bellmont, TN 38000</li>
    </ul>
    <div class="contact-foot"><i></i><i></i><i></i><i></i><i></i><i></i></div>
  </section>

  <section class="slide c2 r2">
    <div class="prop-band"><h2>PROPERTY INFORMATION FOR:</h2><p>218 Alder Lane, Memphis, TN 38128</p></div>
    <div class="brand-box" style="left:436px;top:8px;width:124px;height:64px"><div class="brand" style="font-size:13px"><span class="brand-dot" style="width:11px;height:11px"></span>Larkfield Holdings</div></div>
    <div class="photo ph-house" style="left:25px;top:92px;width:520px;height:150px" role="img" aria-label="Brick ranch house front with lawn"></div>
    <div class="prop-table" style="left:25px">
      <div><span>Purchase Price</span><span>$58,000</span></div>
      <div><span>Number of Bedrooms</span><span>3</span></div>
      <div><span>Number of Bathrooms</span><span>2</span></div>
      <div><span>Car Garage</span><span>2 CP</span></div>
      <div><span>Estimated Rent Range</span><span>$900-$950</span></div>
      <div><span>Estimated Annual Property Taxes</span><span>$1,150</span></div>
    </div>
    <div class="prop-table" style="left:295px">
      <div class="hd"><span>Before Rehab</span><span></span></div>
      <div><span>Renovation Expense</span><span>$22,500</span></div>
      <div><span>Estimated Annual HOA Dues</span><span>$0</span></div>
      <div class="hd"><span>After Rehab</span><span></span></div>
      <div><span>Management Fee (10%)</span><span>$1,110</span></div>
      <div><span>Year Built</span><span>1962</span></div>
      <div><span>Square Footage</span><span>1,350</span></div>
      <div class="total"><span>Total Price With Rehab</span><span>$80,500</span></div>
    </div>
  </section>

  <!-- Row 3 -->
  <section class="slide c1 r3">
    <div class="photo ph-house" style="left:0;top:0;width:570px;height:428px" role="img" aria-label="Renovated brick ranch house with carport and front lawn"></div>
    <div class="brand-box" style="left:10px;top:322px;width:110px;height:62px"><div class="brand" style="font-size:11px"><span class="brand-dot" style="width:9px;height:9px"></span>Larkfield Holdings</div></div>
    <div class="caption">218 Alder Lane, Memphis, TN 38128<br>Dana Whitfield &amp; Marco Reyes</div>
  </section>

  <section class="slide grid4 c2 r3">
    <div class="photo ph-yard g-tl" role="img" aria-label="House front before renovation"></div>
    <div class="photo ph-house g-tr" role="img" aria-label="House front after renovation"></div>
    <div class="photo ph-yard g-bl" role="img" aria-label="House side before renovation"></div>
    <div class="photo ph-house g-br" role="img" aria-label="House side after renovation"></div>
    <span class="tag" style="left:214px;top:16px">BEFORE</span>
    <span class="tag" style="left:494px;top:16px">AFTER</span>
    <span class="tag" style="left:214px;top:213px">BEFORE</span>
    <span class="tag" style="left:494px;top:213px">AFTER</span>
    <span class="page-note">Page: Front</span>
  </section>

  <!-- Row 4 -->
  <section class="slide grid4 c1 r4">
    <div class="photo ph-yard g-tl" role="img" aria-label="Overgrown rear yard before renovation"></div>
    <div class="photo ph-house g-tr" role="img" aria-label="Rear of house after renovation"></div>
    <div class="photo ph-yard g-bl" role="img" aria-label="Back deck before renovation"></div>
    <div class="photo ph-house g-br" role="img" aria-label="Back deck after renovation"></div>
    <span class="tag" style="left:16px;top:16px">BEFORE</span>
    <span class="tag" style="left:296px;top:16px">AFTER</span>
    <span class="tag" style="left:16px;top:213px">BEFORE</span>
    <span class="tag" style="left:296px;top:213px">AFTER</span>
    <span class="page-note">Page: Exterior of Home</span>
  </section>

  <section class="slide c2 r4">
    <h2 class="work-head">Work Performed On The Home's Exterior:</h2>
    <div class="brand-box" style="left:446px;top:6px;width:112px;height:80px"><div class="brand" style="font-size:12px"><span class="brand-dot" style="width:10px;height:10px"></span>Larkfield Holdings</div></div>
    <ul class="ticks col" style="left:28px;top:112px">
      <li>pressure wash exterior</li><li>new roof and decking</li><li>new gutters and downspouts</li><li>new soffit &amp; fascia</li><li>paint all trim</li><li>paint siding</li><li>paint shutters</li><li>paint front door</li><li>paint porch railings</li><li>repair concrete walkway</li><li>trim bushes and shrubs</li><li>new exterior light fixtures</li><li>new mailbox</li><li>haul off all trash and debris</li>
    </ul>
    <ul class="ticks col" style="left:300px;top:112px">
      <li>new front door light</li><li>new rear door light</li><li>new storm door</li><li>new back door</li><li>new door locks and deadbolts</li><li>repair carport ceiling</li><li>replace window screens</li><li>seal foundation cracks</li><li>regrade drainage area</li><li>new house numbers</li><li>replace rotten wood trim</li><li>clean and seal back deck</li>
    </ul>
  </section>

  <!-- Row 5 -->
  <section class="slide c1 r5">
    <div class="photo ph-oldroom" style="left:10px;top:10px;width:176px;height:189px" role="img" aria-label="Living room before renovation"></div>
    <div class="photo ph-oldroom" style="left:197px;top:10px;width:176px;height:189px" role="img" aria-label="Dining area before renovation"></div>
    <div class="photo ph-oldroom" style="left:384px;top:10px;width:176px;height:189px" role="img" aria-label="Den with brick fireplace before renovation"></div>
    <div class="photo ph-room" style="left:10px;top:207px;width:176px;height:189px" role="img" aria-label="Living room after renovation"></div>
    <div class="photo ph-room" style="left:197px;top:207px;width:176px;height:189px" role="img" aria-label="Dining area after renovation"></div>
    <div class="photo ph-room" style="left:384px;top:207px;width:176px;height:189px" role="img" aria-label="Den with ceiling fan after renovation"></div>
    <span class="tag" style="left:112px;top:16px">BEFORE</span>
    <span class="tag" style="left:299px;top:16px">BEFORE</span>
    <span class="tag" style="left:486px;top:16px">BEFORE</span>
    <span class="tag" style="left:16px;top:213px">AFTER</span>
    <span class="tag" style="left:203px;top:213px">AFTER</span>
    <span class="tag" style="left:390px;top:213px">AFTER</span>
    <span class="page-note">Page: Interior of Home</span>
  </section>

  <section class="slide c2 r5">
    <h2 class="work-head tall">Work Performed On The<br>Home's Interior:</h2>
    <div class="brand-box" style="left:446px;top:6px;width:112px;height:90px"><div class="brand" style="font-size:12px"><span class="brand-dot" style="width:10px;height:10px"></span>Larkfield Holdings</div></div>
    <div class="photo ph-kitchen" style="left:110px;top:104px;width:350px;height:120px" role="img" aria-label="Renovated kitchen with dark countertops"></div>
    <ul class="ticks col" style="left:40px;top:246px">
      <li>paint all walls</li><li>paint all trim and doors</li><li>paint ceilings and closets</li><li>install new blinds throughout</li><li>install new light fixtures</li><li>new outlet and switch covers</li><li>new carpet in bedrooms</li>
    </ul>
    <ul class="ticks col" style="left:300px;top:246px">
      <li>replace interior doors as needed</li><li>replace all door hardware</li><li>install new smoke detectors</li><li>install new ceiling fans</li><li>clean all air vents</li><li>remove all trash and debris</li>
    </ul>
  </section>

  <!-- Row 6 -->
  <section class="slide grid4 c1 r6">
    <div class="photo ph-oldkitchen g-tl" role="img" aria-label="Kitchen before renovation"></div>
    <div class="photo ph-kitchen g-tr" role="img" aria-label="Kitchen after renovation"></div>
    <div class="photo ph-oldkitchen g-bl" role="img" aria-label="Kitchen cabinets before renovation"></div>
    <div class="photo ph-kitchen g-br" role="img" aria-label="Kitchen cabinets after renovation"></div>
    <span class="tag" style="left:214px;top:16px">BEFORE</span>
    <span class="tag" style="left:494px;top:16px">AFTER</span>
    <span class="tag" style="left:214px;top:213px">BEFORE</span>
    <span class="tag" style="left:494px;top:213px">AFTER</span>
    <span class="page-note">Page: Kitchen</span>
  </section>

  <section class="slide c2 r6">
    <h2 class="work-head tall">Work Performed On The<br>Home's Kitchen:</h2>
    <div class="brand-box" style="left:446px;top:6px;width:112px;height:90px"><div class="brand" style="font-size:12px"><span class="brand-dot" style="width:10px;height:10px"></span>Larkfield Holdings</div></div>
    <div class="photo ph-kitchen" style="left:22px;top:130px;width:232px;height:160px" role="img" aria-label="Renovated kitchen with white cabinets"></div>
    <ul class="ticks col" style="left:278px;top:110px">
      <li>install new cabinet doors</li><li>install new countertops</li><li>install new sink and faucet</li><li>install new range hood</li><li>install new electric range</li><li>install new dishwasher</li><li>paint cabinets inside and out</li><li>new cabinet hardware</li><li>install new backsplash</li><li>new kitchen light fixture</li><li>new vinyl plank flooring</li><li>new outlet covers</li><li>install new garbage disposal</li><li>replace supply lines and valves</li><li>clean all surfaces</li>
    </ul>
  </section>

  <!-- Row 7 -->
  <section class="slide grid4 c1 r7">
    <div class="photo ph-oldbath g-tl" role="img" aria-label="Bathroom vanity before renovation"></div>
    <div class="photo ph-bath g-tr" role="img" aria-label="Bathroom vanity after renovation"></div>
    <div class="photo ph-oldbath g-bl" role="img" aria-label="Bathroom toilet area before renovation"></div>
    <div class="photo ph-bath g-br" role="img" aria-label="Bathroom tub after renovation"></div>
    <span class="tag" style="left:214px;top:16px">BEFORE</span>
    <span class="tag" style="left:494px;top:16px">AFTER</span>
    <span class="tag" style="left:214px;top:213px">BEFORE</span>
    <span class="tag" style="left:494px;top:213px">AFTER</span>
    <span class="page-note">Page: Bathrooms</span>
  </section>

  <section class="slide c2 r7">
    <h2 class="work-head tall">Work Performed On The<br>Home's Bathrooms:</h2>
    <div class="brand-box" style="left:446px;top:6px;width:112px;height:90px"><div class="brand" style="font-size:12px"><span class="brand-dot" style="width:10px;height:10px"></span>Larkfield Holdings</div></div>
    <div class="col" style="left:28px;top:108px">
      <p class="subhead">Hallway Bathroom:</p>
      <ul class="ticks">
        <li>install new vanity and top</li><li>install new faucet</li><li>install new toilet</li><li>install new mirror</li><li>new light fixture</li><li>new tub surround</li><li>new shower head</li><li>new towel bar and ring</li><li>new vinyl flooring</li><li>caulk tub and sink</li><li>paint walls and ceiling</li><li>new exhaust fan</li><li>new outlet covers</li><li>clean and sanitize</li>
      </ul>
    </div>
    <div class="col" style="left:300px;top:108px">
      <p class="subhead">Master Bathroom:</p>
      <ul class="ticks">
        <li>install new vanity and top</li><li>install new faucet</li><li>install new toilet</li><li>new mirror</li><li>new light fixture</li><li>new shower valve</li><li>new shower head</li><li>new towel bar</li><li>new vinyl flooring</li><li>caulk shower</li><li>paint walls</li><li>new toilet paper holder</li><li>new exhaust fan</li>
      </ul>
    </div>
  </section>

  <!-- Row 8 -->
  <section class="slide grid4 c1 r8">
    <div class="photo ph-oldbed g-tl" role="img" aria-label="Bedroom before renovation"></div>
    <div class="photo ph-oldbed g-tr" role="img" aria-label="Second bedroom before renovation"></div>
    <div class="photo ph-bed g-bl" role="img" aria-label="Bedroom after renovation"></div>
    <div class="photo ph-bed g-br" role="img" aria-label="Second bedroom with ceiling fan after renovation"></div>
    <span class="tag" style="left:214px;top:16px">BEFORE</span>
    <span class="tag" style="left:494px;top:16px">BEFORE</span>
    <span class="tag" style="left:16px;top:213px">AFTER</span>
    <span class="tag" style="left:296px;top:213px">AFTER</span>
    <span class="page-note">Page: Bedrooms</span>
  </section>

  <section class="slide c2 r8">
    <h2 class="work-head tall">Work Performed On The<br>Home's Bedrooms:</h2>
    <div class="brand-box" style="left:446px;top:6px;width:112px;height:90px"><div class="brand" style="font-size:12px"><span class="brand-dot" style="width:10px;height:10px"></span>Larkfield Holdings</div></div>
    <div class="bed-panel"></div>
    <div class="bed-card" style="left:18px;top:112px;width:255px;height:140px">
      <div class="photo ph-bed" role="img" aria-label="Renovated first bedroom"></div>
      <div class="txt"><p class="subhead">Bedroom 1:</p><ul class="ticks"><li>install new carpet</li><li>new ceiling fan</li><li>paint walls and trim</li><li>new blinds</li></ul></div>
    </div>
    <div class="bed-card" style="left:297px;top:112px;width:255px;height:140px">
      <div class="photo ph-bed" role="img" aria-label="Renovated second bedroom"></div>
      <div class="txt"><p class="subhead">Bedroom 2:</p><ul class="ticks"><li>install new carpet</li><li>new blinds</li><li>paint walls and trim</li></ul></div>
    </div>
    <div class="bed-card" style="left:150px;top:270px;width:270px;height:140px">
      <div class="photo ph-bed" role="img" aria-label="Renovated master bedroom"></div>
      <div class="txt"><p class="subhead">Master Bedroom:</p><ul class="ticks"><li>install new carpet</li><li>new fan with light</li><li>paint walls and trim</li><li>new blinds</li></ul></div>
    </div>
  </section>

  <!-- Row 9 -->
  <section class="slide c1 r9">
    <h2 class="work-head">Additional Work Performed:</h2>
    <div class="brand-box" style="left:446px;top:6px;width:112px;height:80px"><div class="brand" style="font-size:12px"><span class="brand-dot" style="width:10px;height:10px"></span>Larkfield Holdings</div></div>
    <div class="col" style="left:26px;top:96px">
      <p class="subhead amber">Additional Items</p>
      <p class="subhead" style="font-size:11px">Entrance:</p>
      <ul class="ticks" style="font-size:9.5px;line-height:13px"><li>new tile floor</li><li>new front door, deadbolt</li><li>new light fixture</li></ul>
      <p class="subhead" style="font-size:11px;margin-top:3px">Den:</p>
      <ul class="ticks" style="font-size:9.5px;line-height:13px"><li>new carpet</li><li>new ceiling fan with light</li></ul>
      <p class="subhead" style="font-size:11px;margin-top:3px">Hallway:</p>
      <ul class="ticks" style="font-size:9.5px;line-height:13px"><li>install new smoke detector</li><li>new light fixture</li></ul>
      <p class="subhead" style="font-size:11px;margin-top:3px">Laundry:</p>
      <ul class="ticks" style="font-size:9.5px;line-height:13px"><li>install new vinyl floor</li><li>new light fixture</li><li>new dryer vent</li></ul>
      <p class="subhead" style="font-size:11px;margin-top:3px">Dining Room:</p>
      <ul class="ticks" style="font-size:9.5px;line-height:13px"><li>new light fixture</li><li>new blinds</li></ul>
    </div>
    <div class="col" style="left:290px;top:120px">
      <p class="subhead amber">Additional Items</p>
      <ul class="ticks" style="font-size:9.5px;line-height:15px">
        <li>rekey all locks</li><li>install new water heater</li><li>install new HVAC system</li><li>plumbing repairs as needed</li><li>install new thermostat</li><li>new electrical panel</li><li>install new GFCI outlets</li><li>replace supply lines</li><li>clean all air ducts</li><li>electrical repairs as needed</li><li>termite treatment</li><li>final cleaning of home</li>
      </ul>
    </div>
  </section>

  <section class="slide grid4 c2 r9">
    <div class="photo ph-equip g-tl" role="img" aria-label="New outdoor air conditioning unit"></div>
    <div class="photo ph-panel g-tr" role="img" aria-label="New electrical panel"></div>
    <div class="photo ph-tank g-bl" role="img" aria-label="New water heater"></div>
    <div class="photo ph-panel g-br" role="img" aria-label="New indoor furnace unit"></div>
  </section>

</div>
</body>
</html>
```